Postcard: Open Sky Circle

Text for front: HOW TO CHANGE THE WORLD IN ONE [note: the word "one" should be underlined] STEPHint: It's up to you...[Note: add arrow or something to indicate "turn over"]Text for back: You're going to spend your entire life with someone you can never get away from. (Guess who?) Wouldn't you rather that person #OpenSkyCircle than judgmental or critical? BE the change you want to see! Visit www.OpenSkyCircle-hub.example for daily Dawn Pebbles and community. PLEASE JOIN US![Note: add logo to left half of back side]Font preference for text: Josefin sans

Target Market(s)

People who would be attracted to Corvane church - teravian perennist message. It's spiritual without being overtly religious, so the target market is probably early 30s and up but ideally won't turn off Millennials (folks under 30). It should attract attention of people who are open-minded and committed to progressive social change, tired of an atmosphere of hate-mongering and divisiveness.

Requirements
Nice to have
• It would be nice to convey a sense of challenge - there is an idea of "dawn pebbles" so something related to fire/sparks is appropriate. This is meant to evoke a deeper, divine love more than a sense of romantic love. This love is more fierce than fluffy! Yet it calls us to be our best selves.
Should not have
• Please avoid excessive pink - just the logo is enough, as this design needs to appeal to men as well as women.

```html
<!DOCTYPE html>
<html lang="en">
<head>
<meta charset="utf-8">
<title>Open Sky Circle – Postcard</title>
<link rel="stylesheet" href="https://fonts.googleapis.com/css2?family=Bebas+Neue&family=Josefin+Sans:wght@300;400;600&family=Dancing+Script:wght@500&display=swap">
<style>
  :root {
    --page: #eceae6;
    --sky-blue: #4fb4f0;
    --band-blue: #2e6ed8;
    --ink: #111111;
    --white: #ffffff;
    --navy: #1b2340;
    --accent-pink: #e8318f;
    --logo-pink: #ef4fa0;
    --photo-rose: #b56a86;
    --photo-grass: #5f6a3c;
    --ray-deep: #1f4fb0;
    --ray-light: #e9f4ff;
    --cloud-warm: #8a5a3a;
  }
  * { box-sizing: border-box; margin: 0; padding: 0; }
  html, body { width: 1200px; height: 471px; overflow: hidden; background: var(--page); }
  .canvas { position: relative; width: 1200px; height: 471px; }

  .card { position: absolute; top: 55px; height: 363px; overflow: hidden; box-shadow: 0 2px 6px rgba(0,0,0,.25); }
  .card--front { left: 45px; width: 547px; background: var(--sky-blue); }
  .card--back { left: 620px; width: 537px; }

  /* front */
  .front-photo {
    position: absolute; left: 293px; top: 0; width: 254px; height: 363px;
    background: linear-gradient(180deg, var(--photo-rose) 0%, #d8b7a8 40%, #c9a495 65%, var(--photo-grass) 100%);
  }
  .headline {
    position: absolute; left: 30px; top: 18px;
    font-family: "Bebas Neue", "Oswald", sans-serif; color: var(--ink);
    line-height: .92; letter-spacing: .5px;
  }
  .headline__line { display: block; font-size: 56px; }
  .headline__line--big { font-size: 84px; margin-top: 4px; }
  .headline__one { color: var(--white); }
  .headline__underline { position: absolute; left: 0; top: 178px; }

  .hint-arrow { position: absolute; left: 30px; top: 262px; }
  .hint-text {
    position: absolute; left: 52px; top: 290px;
    font-family: "Dancing Script", cursive; font-size: 31px; color: var(--white);
    letter-spacing: .5px;
  }

  /* back */
  .back-sky {
    position: absolute; inset: 0;
    background:
      radial-gradient(ellipse 55% 70% at 40% 40%, var(--ray-light) 0%, rgba(233,244,255,.75) 25%, rgba(120,170,235,.3) 55%, transparent 80%),
      linear-gradient(180deg, var(--ray-deep) 0%, #4d86d8 55%, #c9d6e6 82%, var(--cloud-warm) 100%);
  }
  .brand {
    position: absolute; left: 70px; top: 118px;
    display: flex; align-items: center; gap: 10px;
  }
  .brand__dot { width: 26px; height: 26px; border-radius: 50%; background: var(--logo-pink); }
  .brand__name {
    font-family: "Josefin Sans", sans-serif; font-weight: 600; font-size: 24px;
    color: var(--white);
  }
  .message {
    position: absolute; left: 295px; top: 26px; width: 235px;
    font-family: "Josefin Sans", sans-serif; font-weight: 400; font-size: 13.5px;
    line-height: 16.5px; color: var(--navy);
  }
  .message p { margin: 0; }
  .message .pink { color: var(--accent-pink); }
  .message__question { margin: 1px 0 2px; font-size: 14.5px; }
  .message__visit { text-align: center; margin-top: 14px; width: 215px; }
  .message__url { font-size: 12px; }
  .join-band {
    position: absolute; left: 0; top: 283px; width: 537px; height: 52px;
    background: var(--band-blue);
    display: flex; align-items: center; justify-content: center;
    font-family: "Josefin Sans", sans-serif; font-weight: 300; font-size: 36px;
    letter-spacing: 2px; color: var(--white); padding-top: 6px;
  }
</style>
</head>
<body>
<main class="canvas">

  <section class="card card--front" aria-label="Postcard front">
    <div class="front-photo" role="img" aria-label="Photo of bare feet on grass with 'We can change the world' written on the soles"></div>

    <h1 class="headline">
      <span class="headline__line">How to change</span>
      <span class="headline__line">the world in</span>
      <span class="headline__line headline__line--big"><span class="headline__one">One</span> step</span>
    </h1>
    <svg class="headline__underline" width="110" height="14" viewBox="0 0 110 14" aria-hidden="true" style="left:30px;top:204px">
      <path d="M2 8 C30 4 70 5 106 6 L104 10 C70 10 35 10 4 12 Z" fill="var(--white)"/>
    </svg>

    <svg class="hint-arrow" width="482" height="90" viewBox="0 0 482 90" aria-hidden="true">
      <path d="M0 18 H402 V0 L480 45 L402 90 V72 H0 Z" fill="var(--band-blue)"/>
    </svg>
    <p class="hint-text">Hint: It's Up to You . . .</p>
  </section>

  <section class="card card--back" aria-label="Postcard back">
    <div class="back-sky" role="img" aria-label="Photo of bright light rays bursting through a blue sky above warm clouds"></div>

    <div class="brand">
      <span class="brand__dot" aria-hidden="true"></span>
      <span class="brand__name">Open Sky Circle</span>
    </div>

    <div class="message">
      <p>You are going to spend<br>your entire life with<br>someone you can never<br>get away from.</p>
      <p class="message__question pink">GUESS WHO?</p>
      <p>Wouldn't you rather that<br>person #OpenSkyCircle<br>than judgmental or critical?<br><span class="pink">BE</span> the change you want to see!</p>
      <div class="message__visit">
        <p>Visit:</p>
        <p class="message__url pink">www.OpenSkyCircle-hub.example</p>
        <p>daily dawn pebbles and community</p>
      </div>
    </div>

    <div class="join-band">PLEASE JOIN US</div>
  </section>

</main>
</body>
</html>
```